Tarjetas de visita para empresa de aluminio

Empresa con mas de 40 años vendiendo perfiles de aluminio.
Somos fábrica y almacén, queremos renovar la tarjeta de presentación de nuestros comerciales dando una imgen innovadora y tecnógica mezclado con la calidez del respeto al medio ambiente.
Añado el logo de la empresa y actual cara trasera de la tarjeta de visita, el logo es el simbolo WM y la marca TRAVENIC EXTRUSION, la frase 2extrusion y lacado de aluminio" debe cambiarse por "Diseño, extrusión, lacado, anodizado y mecanizado de precisión de aluminio" o en su defecto incluir todos esos servicios que hacemos o una frase mas pegadiza.

We are an aluminium factory, we produce and stock profiles of aluminium.
we want to renew visit card of our sellers, we are looking for something that show innovation, tecnology and environment respect.
Upload our actual logo and back of visit card, logo WM and brand TRAVENIC EXTRUSION must be keept.
Text "Extrusion y lacado de aluminio" must be changed for "Diseño, extrusion, lacado, anodizado y mecanizado de precisión de aluminio" or something like that

```html
<!DOCTYPE html>
<html lang="es">
<head>
<meta charset="utf-8">
<title>Tarjetas de visita – Travenic Extrusion</title>
<link href="https://fonts.googleapis.com/css2?family=Montserrat:wght@400;500;600;700&display=swap" rel="stylesheet">
<style>
  :root {
    --brand-blue: #2b5a84;
    --white: #ffffff;
    --page: #ffffff;
    --silver-light: #f4f4f4;
    --silver-mid: #c9c9c9;
    --silver-dark: #8f8f8f;
  }
  html, body {
    margin: 0;
    padding: 0;
    width: 1200px;
    height: 1200px;
    overflow: hidden;
    background: var(--page);
  }
  .sheet { display: block; width: 1200px; height: 1200px; }
  .card-base { fill: var(--brand-blue); }
  .wave-band { fill: var(--brand-blue); stroke: var(--white); stroke-width: 5; }
  .person-name {
    font-family: "Montserrat", sans-serif;
    font-weight: 700;
    font-size: 46px;
    letter-spacing: 1px;
  }
  .person-role {
    font-family: "Montserrat", sans-serif;
    font-weight: 500;
    font-size: 27px;
    fill: var(--white);
    letter-spacing: 0.5px;
  }
  .role-rule { fill: var(--white); }
  .contact-text {
    font-family: "Montserrat", sans-serif;
    font-weight: 400;
    font-size: 24px;
    fill: var(--white);
  }
  .icon-disc { fill: var(--white); }
  .icon-glyph { fill: var(--brand-blue); }
  .icon-line { fill: none; stroke: var(--brand-blue); stroke-width: 1.8; }
  .social-disc { fill: var(--white); }
  .brand-mark {
    font-family: "Montserrat", sans-serif;
    font-weight: 700;
    font-size: 92px;
    letter-spacing: 4px;
  }
  .brand-mark--front { fill: var(--brand-blue); }
  .brand-mark--back { fill: var(--white); }
  .brand-name {
    font-family: "Montserrat", sans-serif;
    font-weight: 700;
    font-size: 34px;
    letter-spacing: 4px;
    fill: var(--white);
  }
  .brand-tagline {
    font-family: "Montserrat", sans-serif;
    font-weight: 500;
    font-size: 22px;
    letter-spacing: 1px;
    fill: var(--white);
  }
</style>
</head>
<body>
<svg class="sheet" viewBox="0 0 1500 1500" xmlns="http://www.w3.org/2000/svg" aria-label="Tarjetas de visita de Travenic Extrusion, anverso y reverso">
  <defs>
    <linearGradient id="silverFront" x1="640" y1="600" x2="1200" y2="200" gradientUnits="userSpaceOnUse">
      <stop offset="0" stop-color="#9a9a9a"/>
      <stop offset="0.35" stop-color="#e2e2e2"/>
      <stop offset="0.55" stop-color="#ffffff"/>
      <stop offset="0.8" stop-color="#cfcfcf"/>
      <stop offset="1" stop-color="#a9a9a9"/>
    </linearGradient>
    <linearGradient id="silverBack" x1="230" y1="900" x2="860" y2="1200" gradientUnits="userSpaceOnUse">
      <stop offset="0" stop-color="#a8a8a8"/>
      <stop offset="0.4" stop-color="#dcdcdc"/>
      <stop offset="0.6" stop-color="#ffffff"/>
      <stop offset="0.85" stop-color="#b8b8b8"/>
      <stop offset="1" stop-color="#8a8a8a"/>
    </linearGradient>
    <linearGradient id="nameSilver" x1="0" y1="220" x2="0" y2="262" gradientUnits="userSpaceOnUse">
      <stop offset="0" stop-color="#ffffff"/>
      <stop offset="0.5" stop-color="#d6d6d6"/>
      <stop offset="1" stop-color="#a4a4a4"/>
    </linearGradient>
    <clipPath id="frontClip">
      <path d="M278,125 H985 C1160,125 1272,270 1272,423 C1272,590 1150,722 985,722 H278 Q218,722 218,662 V185 Q218,125 278,125 Z"/>
    </clipPath>
    <clipPath id="backClip">
      <path d="M505,765 H1210 Q1270,765 1270,825 V1305 Q1270,1365 1210,1365 H505 C340,1365 220,1230 220,1065 C220,900 340,765 505,765 Z"/>
    </clipPath>
  </defs>

  <!-- Front card -->
  <g class="card card--front">
    <g clip-path="url(#frontClip)">
      <rect class="card-base" x="200" y="110" width="1100" height="630"/>
      <path fill="url(#silverFront)" d="M1150,160 C1040,300 900,412 650,414 C760,470 870,625 1010,633 C1130,640 1220,560 1290,470 V160 Z"/>
      <path class="wave-band" d="M200,535 C320,460 430,386 520,388 C600,390 660,420 720,460 C820,540 900,625 1010,633 C1130,640 1220,560 1285,470 V760 H200 Z"/>
      <text class="brand-mark brand-mark--front" x="1030" y="525" text-anchor="middle">WM</text>
    </g>

    <text class="person-name" x="322" y="258" fill="url(#nameSilver)">MARCOS LERA ORTIZ</text>
    <text class="person-role" x="322" y="302">COMERCIAL</text>
    <rect class="role-rule" x="322" y="322" width="102" height="4"/>

    <g class="contact-list">
      <g class="contact-item">
        <circle class="icon-disc" cx="335" cy="495" r="15"/>
        <path class="icon-glyph" d="M328,487 q3,-3 5,0 l2,3 q1,2 -1,3 l-1,1 q2,4 6,6 l1,-1 q1,-2 3,-1 l3,2 q3,2 0,5 l-2,2 q-4,2 -11,-4 q-7,-7 -6,-12 z"/>
        <text class="contact-text" x="367" y="503">655 20 47 13</text>
      </g>
      <g class="contact-item">
        <circle class="icon-disc" cx="335" cy="533" r="15"/>
        <rect class="icon-line" x="326" y="527" width="18" height="12" rx="1.5"/>
        <path class="icon-line" d="M326,528 L335,535 L344,528"/>
        <text class="contact-text" x="367" y="541">marcoslera@travenic.com</text>
      </g>
      <g class="contact-item">
        <circle class="icon-disc" cx="335" cy="570" r="15"/>
        <circle class="icon-line" cx="335" cy="570" r="9"/>
        <ellipse class="icon-line" cx="335" cy="570" rx="4" ry="9"/>
        <path class="icon-line" d="M326,570 H344 M328,565 H342 M328,575 H342"/>
        <text class="contact-text" x="367" y="578">www.travenic.com</text>
      </g>
      <g class="contact-item">
        <path class="icon-disc" d="M335,624 C331,618 322,611 322,602 A13,13 0 0 1 348,602 C348,611 339,618 335,624 Z"/>
        <circle class="icon-glyph" cx="335" cy="602" r="5"/>
        <text class="contact-text" x="367" y="613">Pol. Ind. Nervia - C/4 No 22</text>
        <text class="contact-text" x="367" y="648">41590 VILLAREAL DEL RÍO (Sevilla)</text>
        <text class="contact-text" x="367" y="683">Apartado de Correos 305</text>
      </g>
    </g>
  </g>

  <!-- Back card -->
  <g class="card card--back">
    <g clip-path="url(#backClip)">
      <rect class="card-base" x="200" y="750" width="1100" height="630"/>
      <path fill="url(#silverBack)" d="M345,800 C420,960 600,1062 860,1058 C720,1100 560,1285 420,1285 C330,1285 260,1210 200,1120 V800 Z"/>
      <path class="wave-band" d="M200,1110 C260,1210 330,1285 420,1285 C600,1285 800,1030 990,1030 C1120,1030 1210,1120 1285,1180 V1380 H200 Z"/>
    </g>

    <g class="social-row">
      <circle class="social-disc" cx="677" cy="872" r="26"/>
      <circle class="social-disc" cx="760" cy="872" r="26"/>
      <circle class="social-disc" cx="843" cy="872" r="26"/>
      <circle class="social-disc" cx="927" cy="872" r="26"/>
    </g>

    <g class="web-line">
      <circle class="icon-disc" cx="685" cy="954" r="15"/>
      <circle class="icon-line" cx="685" cy="954" r="9"/>
      <ellipse class="icon-line" cx="685" cy="954" rx="4" ry="9"/>
      <path class="icon-line" d="M676,954 H694 M678,949 H692 M678,959 H692"/>
      <text class="contact-text" x="718" y="962">www.travenic.com</text>
    </g>

    <text class="brand-mark brand-mark--back" x="985" y="1178" text-anchor="middle">WM</text>
    <text class="brand-name" x="985" y="1256" text-anchor="middle">TRAVENIC EXTRUSION</text>
    <text class="brand-tagline" x="985" y="1295" text-anchor="middle">Diseño, extrusion, lacado, anodizado</text>
    <text class="brand-tagline" x="985" y="1323" text-anchor="middle">y mecanizado de precisión de aluminio</text>
  </g>
</svg>
</body>
</html>
```